依頼詳細
イラストを3点募集します。
1:会社で排出するゴミを減らすために、食べ終わったコンビニの弁当やコンビニのコーヒーカップを洗って重ねることで、体積を減らし、ゴミの排出量を減らす取り組みをする予定です。その際に一般の従業員にもわかるようなイラストを募集します。ラフ画があります。

2:食事後の弁当容器やコーヒーカップなどを洗うようなイラストを募集します。
ラフ画がありません。

3:コンビニなどの袋にまとめて、ゴミ箱へ捨てることを禁止するイラストを募集します。
ラフ画がありません。

イラスト数
3点
希望イメージ
シンプル 複雑
単色 カラフル
暗い 明るい
日常 高級
遊び心 厳粛
未来的 伝統的
女性的 男性的
希望する色
緑系、青系、水色系
納品ファイル
• イラストレーター形式 (.ai)
• PNG形式 (.png)
補足説明

分別だけ頭にありましたが、注意喚起のPOPを作成した方がよいと提案され、その通りだと思いました。

ありがとうございます。

```html
<!DOCTYPE html>
<html lang="ja">
<head>
<meta charset="utf-8">
<title>分別しよう！ゴミ分別棚</title>
<link href="https://fonts.googleapis.com/css2?family=M+PLUS+Rounded+1c:wght@700;800&display=swap" rel="stylesheet">
<style>
  :root {
    --green: #2f8a3c;
    --green-light: #c9e07a;
    --shelf-bg: #d3e3e9;
    --white: #ffffff;
    --mascot: #c5d93a;
    --cup: #f3f1c8;
  }
  html, body {
    margin: 0;
    padding: 0;
    width: 849px;
    height: 1200px;
    overflow: hidden;
    background: var(--white);
  }
  .poster {
    display: block;
    width: 849px;
    height: 1200px;
    font-family: "M PLUS Rounded 1c", sans-serif;
    font-weight: 800;
  }
  .frame { fill: var(--green); }
  .compartment { fill: var(--shelf-bg); }
  .box { fill: var(--white); stroke: var(--green); stroke-width: 5; }
  .label { fill: var(--green); font-size: 26px; }
  .label-lg { fill: var(--green); font-size: 38px; }
  .size-badge { fill: var(--green); }
  .size-text { fill: var(--white); font-size: 28px; }
  .bin { fill: var(--white); stroke: var(--green); stroke-width: 6; stroke-linejoin: round; }
  .bin-label { fill: var(--green); font-size: 36px; }
  .bin-label-sm { fill: var(--green); font-size: 30px; }
  .icon { fill: var(--green); }
  .icon-line { stroke: var(--green); stroke-width: 7; stroke-linecap: round; fill: none; }
  .bubble { fill: var(--white); stroke: var(--green); stroke-width: 6; stroke-linejoin: round; }
  .bubble-main { fill: var(--green); font-size: 42px; }
  .bubble-sub { fill: var(--green); font-size: 26px; }
  .mascot { fill: var(--mascot); stroke: var(--green); stroke-width: 5; }
  .cup-figure { fill: var(--cup); stroke: var(--green); stroke-width: 4; }
</style>
</head>
<body>
<svg class="poster" viewBox="0 0 849 1200" xmlns="http://www.w3.org/2000/svg">
  <!-- shelf frame -->
  <rect class="frame" x="34" y="93" width="781" height="1052"/>
  <rect class="compartment" x="56" y="113" width="737" height="221"/>
  <rect class="compartment" x="56" y="362" width="737" height="176"/>
  <rect class="compartment" x="56" y="566" width="737" height="170"/>
  <rect class="compartment" x="56" y="770" width="737" height="350"/>

  <!-- top shelf -->
  <rect class="box" x="88" y="252" width="152" height="82"/>
  <text class="label" x="104" y="290">その他</text>

  <g role="img" aria-label="緑の分別キャラクター">
    <rect class="mascot" x="552" y="178" width="126" height="140" rx="14"/>
  </g>
  <g role="img" aria-label="カップのキャラクター">
    <path class="cup-figure" d="M684 252 L752 252 L742 334 L694 334 Z"/>
  </g>

  <path class="bubble" d="M440 158 C500 158 540 180 540 212 C540 224 534 234 524 242 L566 262 L510 252 C492 262 468 266 440 266 C380 266 340 244 340 212 C340 180 380 158 440 158 Z"/>
  <text class="bubble-main" x="440" y="212" text-anchor="middle">分別</text>
  <text class="bubble-sub" x="440" y="246" text-anchor="middle">しよう!</text>

  <!-- coffee cup shelf -->
  <g>
    <rect class="box" x="88" y="412" width="152" height="126"/>
    <text class="label" x="104" y="448">コーヒー</text>
    <text class="label" x="104" y="478">カップ</text>
    <circle class="size-badge" cx="164" cy="510" r="22"/>
    <text class="size-text" x="164" y="520" text-anchor="middle">大</text>
  </g>
  <g>
    <rect class="box" x="264" y="412" width="152" height="126"/>
    <text class="label" x="280" y="448">コーヒー</text>
    <text class="label" x="280" y="478">カップ</text>
    <circle class="size-badge" cx="340" cy="510" r="22"/>
    <text class="size-text" x="340" y="520" text-anchor="middle">中</text>
  </g>
  <g>
    <rect class="box" x="440" y="412" width="152" height="126"/>
    <text class="label" x="456" y="448">コーヒー</text>
    <text class="label" x="456" y="478">カップ</text>
    <circle class="size-badge" cx="516" cy="510" r="22"/>
    <text class="size-text" x="516" y="520" text-anchor="middle">小</text>
  </g>

  <!-- bento shelf -->
  <g>
    <rect class="box" x="88" y="602" width="152" height="134"/>
    <text class="label-lg" x="104" y="650">弁当</text>
    <circle class="size-badge" cx="164" cy="694" r="22"/>
    <text class="size-text" x="164" y="704" text-anchor="middle">大</text>
  </g>
  <g>
    <rect class="box" x="264" y="602" width="152" height="134"/>
    <text class="label-lg" x="280" y="650">弁当</text>
    <circle class="size-badge" cx="340" cy="694" r="22"/>
    <text class="size-text" x="340" y="704" text-anchor="middle">中</text>
  </g>
  <g>
    <rect class="box" x="440" y="602" width="152" height="134"/>
    <text class="label-lg" x="456" y="650">弁当</text>
    <circle class="size-badge" cx="516" cy="694" r="22"/>
    <text class="size-text" x="516" y="704" text-anchor="middle">小</text>
  </g>
  <rect class="box" x="614" y="602" width="152" height="134"/>

  <!-- bins -->
  <g>
    <path class="bin" d="M86 790 L298 790 L286 1118 L98 1118 Z"/>
    <text class="bin-label" x="192" y="858" text-anchor="middle">紙ゴミ</text>
    <path class="icon" d="M192 1036 C204 1052 214 1062 214 1078 C214 1092 204 1102 192 1102 C180 1102 170 1092 170 1078 C170 1066 178 1060 182 1050 C186 1060 190 1062 192 1064 C194 1056 194 1046 192 1036 Z"/>
  </g>
  <g>
    <path class="bin" d="M320 790 L532 790 L520 1118 L332 1118 Z"/>
    <text class="bin-label-sm" x="426" y="838" text-anchor="middle">プラスチック</text>
    <text class="bin-label-sm" x="426" y="874" text-anchor="middle">ビニール</text>
    <text class="bin-label-sm" x="426" y="910" text-anchor="middle">生ゴミ</text>
    <text class="bin-label-sm" x="426" y="946" text-anchor="middle">その他</text>
    <path class="icon" d="M426 1036 C438 1052 448 1062 448 1078 C448 1092 438 1102 426 1102 C414 1102 404 1092 404 1078 C404 1066 412 1060 416 1050 C420 1060 424 1062 426 1064 C428 1056 428 1046 426 1036 Z"/>
  </g>
  <g>
    <path class="bin" d="M554 790 L766 790 L754 1118 L566 1118 Z"/>
    <text class="bin-label" x="660" y="858" text-anchor="middle">不燃ゴミ</text>
    <path class="icon" d="M660 1044 C668 1056 674 1062 674 1074 C674 1084 668 1090 660 1090 C652 1090 646 1084 646 1074 C646 1066 650 1060 654 1054 C657 1060 659 1062 660 1064 C662 1058 662 1052 660 1044 Z"/>
    <path class="icon-line" d="M632 1042 L688 1100 M688 1042 L632 1100"/>
  </g>
</svg>
</body>
</html>
```